Brightvantage.com tech company website

Current site is www.brightvantage.com. The site will tell you about our company.

Designs we like are:
http://megainfo.quellorix.com
www.trelvo.com
www.morvasket.com

Target Market(s)

B2B

Industry/Entity Type

It Company

Coding

Coded - Design and coding required

Number of Pages Required

5+ page

Requirements
Must have
• We want to entice without giving away too much info. We like graphics and colors. But website must look official and credible.

```html
<!DOCTYPE html>
<html lang="en">
<head>
<meta charset="utf-8">
<title>Brightvantage</title>
<link href="https://fonts.googleapis.com/css2?family=Open+Sans:wght@400;600;700&family=Oswald:wght@500&display=swap" rel="stylesheet">
<style>
:root{
  --navy:#0f3b61;
  --blue:#1d5f92;
  --ink:#333a40;
  --muted:#8b9399;
  --line:#dde2e6;
  --paper:#ffffff;
  --grey:#f1f2f3;
  --footer:#1c1c1c;
  --footer-text:#9a9a9a;
}
*{box-sizing:border-box;margin:0;padding:0}
html,body{width:1200px;height:2384px;overflow:hidden}
body{font-family:"Open Sans",Arial,sans-serif;color:var(--ink);background:var(--paper);position:relative}
.topbar{height:36px;background:var(--navy);color:#cfdbe6;font-size:12px;display:flex;align-items:center;padding:0 160px;gap:28px}
.topbar .social{margin-left:auto;display:flex;gap:14px}
.topbar .social span{width:10px;height:10px;border-radius:50%;background:#cfdbe6;display:block}
.header{height:96px;display:flex;align-items:center;padding:0 160px;border-bottom:1px solid var(--line)}
.brand{display:flex;align-items:center;gap:12px;font-family:"Oswald",sans-serif;font-size:30px;color:var(--navy);letter-spacing:1px}
.brand i{width:26px;height:26px;border-radius:50%;background:var(--blue);display:block}
.nav{margin-left:auto;display:flex;gap:34px;font-size:12px;font-weight:600;color:var(--ink)}
.hero{height:580px;position:relative;background:linear-gradient(100deg,#e4eff7 0%,#b9d6ea 45%,#7fa9c9 100%)}
.hero-photo{position:absolute;right:0;top:0;width:620px;height:580px;background:linear-gradient(90deg,rgba(160,196,222,0) 0%,#8fb2cc 40%,#5d7f99 100%)}
.hero-copy{position:absolute;left:160px;top:180px;width:520px}
.hero h1{font-size:52px;line-height:60px;font-weight:600;color:#fff}
.hero p{font-size:18px;color:#fff;margin:14px 0 34px;line-height:24px}
.btn{display:inline-block;font-size:11px;font-weight:700;padding:11px 22px;letter-spacing:.5px}
.btn-solid{background:var(--navy);color:#fff}
.btn-ghost{border:2px solid #fff;color:#fff;margin-left:14px}
.dots{position:absolute;left:535px;top:528px;width:130px;height:38px;border-radius:19px;background:rgba(255,255,255,.35);display:flex;justify-content:center;align-items:center;gap:14px}
.dots span{width:14px;height:14px;border-radius:50%;background:rgba(255,255,255,.7)}
.dots span.on{background:#fff;box-shadow:0 0 0 3px rgba(255,255,255,.5)}
.features{height:320px;position:relative;display:flex;justify-content:center;gap:40px;padding-top:84px;border-bottom:1px solid var(--line)}
.feature{width:200px;text-align:center}
.feature .icon{width:54px;height:54px;margin:0 auto 22px;border:1px solid var(--line);display:flex;align-items:center;justify-content:center}
.feature .icon.on{background:var(--navy);border-color:var(--navy)}
.feature h3{font-size:13px;font-weight:600;margin-bottom:10px}
.feature p{font-size:11px;color:var(--muted);line-height:17px}
.arrow{position:absolute;top:140px}
.about{height:428px;background:var(--grey);position:relative}
.seal{position:absolute;left:240px;top:78px;width:272px;height:272px;border-radius:50%;background:radial-gradient(circle,#2a4a7a 0 55%,#c9a43b 56% 64%,#1f3b66 65%)}
.about-copy{position:absolute;left:540px;top:64px;width:440px}
.about h2{font-size:22px;font-weight:700;color:var(--navy);letter-spacing:1px;margin-bottom:18px}
.about p{font-size:12px;color:var(--muted);line-height:20px;margin-bottom:14px}
.news{height:540px;text-align:center;padding-top:34px}
.news h2{font-size:24px;font-weight:700;color:var(--navy);letter-spacing:1px}
.news .lead{font-size:12px;color:var(--muted);width:520px;margin:10px auto 0;line-height:19px}
.grid{display:grid;grid-template-columns:432px 432px;gap:30px 40px;justify-content:center;margin-top:34px;text-align:left}
.card{height:140px;display:flex;background:#f6f7f8}
.card.on{background:var(--blue);color:#fff}
.card .rail{width:30px;background:var(--navy);display:flex;flex-direction:column;align-items:center;padding-top:14px;gap:12px}
.card .rail span{width:12px;height:12px;border:2px solid #fff;border-radius:2px}
.card .pic{width:170px}
.card .body{padding:16px 18px;flex:1}
.card h4{font-size:14px;font-weight:700;margin-bottom:10px}
.card p{font-size:11px;line-height:17px;color:var(--muted)}
.card.on p{color:#d8e6f2}
.partners{height:148px;display:flex;justify-content:center;align-items:center;gap:78px;border-top:1px solid var(--line)}
.partners span{width:96px;height:56px;border-radius:28px;border:2px solid #c4c8cc;background:#eceeef}
.partners span:nth-child(odd){border-radius:50%;width:66px;height:66px}
.footer{height:236px;background:var(--footer);color:var(--footer-text);font-size:12px;position:relative}
.footer .cols{display:flex;justify-content:space-between;padding:46px 160px 0;line-height:20px}
.footer .socials{display:flex;justify-content:center;gap:12px;margin-top:34px}
.footer .socials span{width:26px;height:26px;border-radius:50%;background:#4a4a4a}
.footer .socials span.on{background:#2a8fd0}
.footer .copy{text-align:center;font-size:10px;margin-top:18px}
.footer .top{position:absolute;right:116px;top:168px;width:26px;height:26px;background:#000;display:flex;align-items:center;justify-content:center}
</style>
</head>
<body>
<div class="topbar">
  <span>Language: English</span>
  <span>Tel: +1 (555) 013-4420</span>
  <span>hello@brightvantage.com</span>
  <div class="social"><span></span><span></span><span></span><span></span></div>
</div>
<header class="header">
  <div class="brand"><i></i>BRIGHTVANTAGE</div>
  <nav class="nav"><span>HOME</span><span>ABOUT BRIGHTVANTAGE</span><span>PERCEPTION AND INFLUENCE</span><span>CONSULTING</span><span>CONTACT</span></nav>
</header>
<section class="hero">
  <div class="hero-photo" role="img" aria-label="Photo of a businessman examining data through a magnifying glass"></div>
  <div class="hero-copy">
    <h1>Lorem ipsum dolor sit amet, cons</h1>
    <p>Fusce efficitur erat sed risus rutrum semper, arcu sit amet lectus quis, nec sollicitudin nibh.</p>
    <span class="btn btn-solid">CONTACT NOW</span><span class="btn btn-ghost">READ MORE</span>
  </div>
  <div class="dots"><span></span><span class="on"></span><span></span></div>
</section>
<section class="features">
  <svg class="arrow" style="left:120px" width="14" height="24" viewBox="0 0 14 24"><path d="M12 2 2 12l10 10" fill="none" stroke="#9aa2a8" stroke-width="2"/></svg>
  <div class="feature"><div class="icon"><svg width="24" height="24" viewBox="0 0 24 24"><circle cx="12" cy="12" r="9" fill="none" stroke="#1d5f92" stroke-width="2"/><circle cx="12" cy="12" r="3" fill="#1d5f92"/></svg></div><h3>Precision Audience Targeting</h3><p>Etiam sapien nisi luctus quis nunc volutpat in mauris lorem ipsum dolor</p></div>
  <div class="feature"><div class="icon on"><svg width="24" height="24" viewBox="0 0 24 24"><path d="M4 12l5 5L20 6" fill="none" stroke="#fff" stroke-width="3"/></svg></div><h3>Lead Generation</h3><p>Etiam sapien nisi luctus quis nunc volutpat in mauris lorem ipsum dolor</p></div>
  <div class="feature"><div class="icon"><svg width="24" height="24" viewBox="0 0 24 24"><path d="M4 20V12M10 20V6M16 20v-9M22 20V3" stroke="#1d5f92" stroke-width="3"/></svg></div><h3>Data Enhancement</h3><p>Etiam sapien nisi luctus quis nunc volutpat in mauris lorem ipsum dolor</p></div>
  <div class="feature"><div class="icon"><svg width="24" height="24" viewBox="0 0 24 24"><rect x="3" y="6" width="18" height="12" fill="none" stroke="#1d5f92" stroke-width="2"/><circle cx="12" cy="12" r="3" fill="#1d5f92"/></svg></div><h3>Data Monetization</h3><p>Etiam sapien nisi luctus quis nunc volutpat in mauris lorem ipsum dolor</p></div>
  <svg class="arrow" style="right:120px" width="14" height="24" viewBox="0 0 14 24"><path d="M2 2l10 10L2 22" fill="none" stroke="#9aa2a8" stroke-width="2"/></svg>
</section>
<section class="about">
  <div class="seal" role="img" aria-label="Circular gold and navy emblem"></div>
  <div class="about-copy">
    <h2>ABOUT US</h2>
    <p>Brightvantage turns complex data into clear decisions. We help organisations find the right audience, shape perception and build lasting influence through careful analysis and trusted consulting.</p>
    <p>Our team combines targeted marketing, lead generation and data enhancement to give clients a measurable advantage. Every project is handled with discretion, accuracy and a strong focus on results that matter to your business goals.</p>
    <p>We work with partners across industries to unlock new value from information they already own.</p>
    <span class="btn btn-solid">READ MORE</span>
  </div>
</section>
<section class="news">
  <h2>LATEST NEWS</h2>
  <p class="lead">Fusce efficitur erat sed risus rutrum semper, arcu sit amet lectus quis nec sollicitudin nibh vitae dolor.</p>
  <div class="grid">
    <div class="card"><div class="rail"><span></span><span></span></div><div class="pic" role="img" aria-label="Photo of a hand touching a digital screen" style="background:linear-gradient(135deg,#1c3f66,#3f7fb5)"></div><div class="body"><h4>Lorem ipsum dolor sit amet</h4><p>Etiam sapien nisi luctus quis nunc volutpat in mauris. Donec at lorem tempus vitae felis.</p></div></div>
    <div class="card on"><div class="rail"><span></span><span></span></div><div class="pic" role="img" aria-label="Photo of a person working at a computer" style="background:linear-gradient(135deg,#6d8ea8,#c2d4e0)"></div><div class="body"><h4>Consectetur sapien sit</h4><p>Etiam sapien nisi luctus quis nunc volutpat in mauris. Donec at lorem tempus vitae felis.</p></div></div>
    <div class="card"><div class="rail"><span></span><span></span></div><div class="pic" role="img" aria-label="Photo of a glowing network of data lines" style="background:linear-gradient(135deg,#0d3050,#2c79ad)"></div><div class="body"><h4>Lorem ipsum dolor sit amet</h4><p>Etiam sapien nisi luctus quis nunc volutpat in mauris. Donec at lorem tempus vitae felis.</p></div></div>
    <div class="card"><div class="rail"><span></span><span></span></div><div class="pic" role="img" aria-label="Photo of colleagues reviewing work together" style="background:linear-gradient(135deg,#8a6a4a,#d8c3a6)"></div><div class="body"><h4>Lorem ipsum dolor sit amet</h4><p>Etiam sapien nisi luctus quis nunc volutpat in mauris. Donec at lorem tempus vitae felis.</p></div></div>
  </div>
</section>
<section class="partners"><span></span><span></span><span></span><span></span><span></span><span></span></section>
<footer class="footer">
  <div class="cols">
    <div>+1 (555) 013-4420<br>+1 (555) 013-4421</div>
    <div>hello@brightvantage.com<br>www.brightvantage.com</div>
    <div>200 Harbor Lane, Suite 12<br>Fairview, ST 00000</div>
  </div>
  <div class="socials"><span></span><span class="on"></span><span></span><span></span><span></span></div>
  <p class="copy">© Brightvantage. All rights reserved.</p>
  <div class="top"><svg width="12" height="8" viewBox="0 0 12 8"><path d="M1 7l5-5 5 5" fill="none" stroke="#fff" stroke-width="2"/></svg></div>
</footer>
</body>
</html>
```